Business Card template designs

We need a lot of Business card designs.
Your designs will get exposure on our newly opened business-card printing website.
We are committed to quality of paper and packages we use, so they will come up very fancy.

Here is your advantage. We will put the profile of the graphic designer on our site so that you can showcase your designs to people around the world and in Japan.

A profile is not mandatory, although we encourage graphic designers to have a profile to get continuous work in the future.
We are looking forward to having many good designs.

The right of the use of design will be owned by us.
The design may be used to the products other than
business cards.

Target Market(s)

designer,photographer,creator,artist

Industry/Entity Type

Printing

Contact Information for Business Card

The back design is important.
Please check the reference file.

Requirements
Must have
• Please include the following, required information on your business card designs.
• Name: Haruna Okabe
• Title: Designer
• Web: https://www.ketori.co.jp/kt/
• Address: 4-17 Kamiharuta-Cho Meguro-ku, Tokyo
• Email: info@kketori.com
• Phone: 03 4816 3907
• Mobile: 070 2143 6658
• * For Japanese sites, we will convert the text portion to Japanese characters.
• * In case of 28mmx70mm only include Name,Enail,Phone and SNS account(https://www.facebook.com/kketori.com)
• 1. colorful
• 2. simple
• 3. natural
• 4. modern
• 5. cool
• 6. sporty
• Please make variations of the same image with 3-6
• different colors / patterns for one design so that
• customers can compare and choose.
• If you want to use a same picture, please make make
• copies and paste on each different types of design.
Nice to have
• You may also use, the following non-required information.
• Company Name: Ketori, Inc.
• Fax: 03-4173-9620
• Open space for company logo

```html
<!DOCTYPE html>
<html lang="en">
<head>
<meta charset="utf-8">
<title>Ketori business card</title>
<link rel="stylesheet" href="https://fonts.googleapis.com/css2?family=Arimo:wght@400;700&family=Open+Sans:wght@400;600&display=swap">
<style>
  :root {
    --backdrop: #9b9b9b;
    --brand-blue: #072a78;
    --card-light: #e9eaec;
    --ink: #2e2e33;
    --ink-soft: #4a4a52;
    --rule: #9c9ca4;
    --logo-white: #eef0f4;
    --url-tint: #b9c3de;
  }
  * { box-sizing: border-box; margin: 0; padding: 0; }
  html, body {
    width: 1105px;
    height: 1200px;
    overflow: hidden;
    background: var(--backdrop);
  }
  .canvas {
    position: relative;
    width: 1105px;
    height: 1200px;
  }
  .card {
    position: absolute;
    left: 182px;
    width: 747px;
    height: 427px;
    overflow: hidden;
  }
  .card--front { top: 119px; background: var(--card-light); }
  .card--back { top: 635px; background: var(--brand-blue); }

  .brand-band {
    position: absolute;
    left: 0; top: 0;
    width: 100%;
    height: 222px;
    background: var(--brand-blue);
  }
  .wordmark {
    position: absolute;
    left: 0; width: 100%;
    text-align: center;
    font-family: "Open Sans", sans-serif;
    font-weight: 400;
    font-size: 92px;
    letter-spacing: 2px;
    color: var(--logo-white);
    line-height: 1;
  }
  .card--front .wordmark { top: 62px; }
  .card--back .wordmark { top: 176px; }

  .identity {
    position: absolute;
    left: 0; top: 236px;
    width: 100%;
    text-align: center;
  }
  .identity__name {
    font-family: "Open Sans", sans-serif;
    font-weight: 600;
    font-size: 23px;
    color: var(--ink);
    line-height: 30px;
  }
  .identity__title {
    display: flex;
    align-items: center;
    justify-content: center;
    gap: 6px;
    font-family: "Open Sans", sans-serif;
    font-size: 18px;
    color: var(--ink);
    line-height: 22px;
  }
  .identity__title::before,
  .identity__title::after {
    content: "";
    width: 222px;
    height: 1px;
    background: var(--rule);
  }

  .contact-list {
    position: absolute;
    left: 28px; top: 290px;
    list-style: none;
    font-family: "Arimo", sans-serif;
    font-size: 18px;
    color: var(--ink-soft);
  }
  .contact-list li {
    display: flex;
    align-items: center;
    height: 29px;
  }
  .contact-list svg {
    width: 18px; height: 18px;
    margin-right: 11px;
    fill: var(--ink);
  }

  .company-block {
    position: absolute;
    right: 28px; top: 292px;
    text-align: right;
    font-family: "Arimo", sans-serif;
    font-size: 17px;
    line-height: 26px;
    color: var(--ink-soft);
  }
  .company-block__name { font-weight: 700; color: var(--ink); }
  .company-block__web { margin-top: 3px; }

  .back-url {
    position: absolute;
    left: 0; top: 364px;
    width: 100%;
    text-align: center;
    font-family: "Arimo", sans-serif;
    font-size: 17px;
    color: var(--url-tint);
  }
</style>
</head>
<body>
<main class="canvas">

  <section class="card card--front" aria-label="Business card front">
    <div class="brand-band">
      <div class="wordmark">Ketori</div>
    </div>

    <div class="identity">
      <h1 class="identity__name">Haruna Okabe</h1>
      <p class="identity__title">Designer</p>
    </div>

    <ul class="contact-list">
      <li>
        <svg viewBox="0 0 24 24" aria-hidden="true"><path d="M6.6 10.8a15.2 15.2 0 0 0 6.6 6.6l2.2-2.2c.3-.3.7-.4 1-.2 1.1.4 2.3.6 3.6.6.6 0 1 .4 1 1V20c0 .6-.4 1-1 1A17 17 0 0 1 3 4c0-.6.4-1 1-1h3.5c.6 0 1 .4 1 1 0 1.3.2 2.5.6 3.6.1.3 0 .7-.2 1z"/></svg>
        03 4816 3907
      </li>
      <li>
        <svg viewBox="0 0 24 24" aria-hidden="true"><path d="M7 1h10a2 2 0 0 1 2 2v18a2 2 0 0 1-2 2H7a2 2 0 0 1-2-2V3a2 2 0 0 1 2-2zm0 3v14h10V4zm5 15.5a1.2 1.2 0 1 0 0 2.4 1.2 1.2 0 0 0 0-2.4z"/></svg>
        070 2143 6658
      </li>
      <li>
        <svg viewBox="0 0 24 24" aria-hidden="true"><path d="M6 2h10l2 2v5H6zM3 10h18a2 2 0 0 1 2 2v8H1v-8a2 2 0 0 1 2-2zm3 7v5h12v-5z"/></svg>
        03-4173-9620
      </li>
      <li>
        <svg viewBox="0 0 24 24" aria-hidden="true"><path d="M2 5h20v14H2zm2 2v.4l8 5.2 8-5.2V7zm0 2.8V17h16V9.8l-8 5.2z"/></svg>
        info@kketori.com
      </li>
    </ul>

    <address class="company-block" style="font-style: normal;">
      <div class="company-block__name">Ketori, Inc.</div>
      <div>4-17 Kamiharuta-Cho</div>
      <div>Meguro-ku, Tokyo</div>
      <div class="company-block__web">www.ketori.co.jp/kt</div>
    </address>
  </section>

  <section class="card card--back" aria-label="Business card back">
    <div class="wordmark">Ketori</div>
    <p class="back-url">www.ketori.co.jp/kt</p>
  </section>

</main>
</body>
</html>
```